Tidewake Charter Angling Tradeshow Booth

Im looking for a professional and attractive, eye catching trade show booth design

Target Market(s)

professionals who are looking to go on a high end fishing excursion

Industry/Entity Type

sport fishing

Requirements
Must have
• my website (www.tidewakecharterangling,com) my logo,

```html
<!DOCTYPE html>
<html lang="en">
<head>
<meta charset="utf-8">
<title>Tidewake Charter Angling – Tradeshow Booth</title>
<link href="https://fonts.googleapis.com/css2?family=Poppins:wght@300;400;700;800&display=swap" rel="stylesheet">
<style>
  :root {
    --stage: #4a4a4a;
    --ocean-top: #1f69b6;
    --ocean-mid: #1c3f8c;
    --ocean-deep: #161f52;
    --accent: #1a72c8;
    --accent-light: #2a86d8;
    --line: #3b86d4;
    --white: #ffffff;
    --ink: #1b1b1b;
  }
  html, body {
    margin: 0;
    padding: 0;
    width: 1200px;
    height: 2583px;
    overflow: hidden;
    background: var(--stage);
  }
  .booth-graphic {
    position: absolute;
    left: 0;
    top: 689px;
    width: 1200px;
    height: 1205px;
    display: block;
    font-family: "Poppins", sans-serif;
  }
  .site-url { font-weight: 300; font-size: 27px; fill: var(--white); }
  .headline { font-weight: 800; font-size: 104px; fill: var(--white); letter-spacing: 1px; }
  .tagline { font-weight: 400; font-size: 28px; fill: var(--white); }
  .brand-name { font-weight: 700; font-size: 30px; fill: var(--ink); }
</style>
</head>
<body>
<svg class="booth-graphic" viewBox="0 0 1200 1205" xmlns="http://www.w3.org/2000/svg">
  <defs>
    <linearGradient id="ocean" x1="0" y1="0" x2="0" y2="1">
      <stop offset="0" stop-color="var(--ocean-top)"/>
      <stop offset="0.45" stop-color="var(--ocean-mid)"/>
      <stop offset="1" stop-color="var(--ocean-deep)"/>
    </linearGradient>
    <linearGradient id="catch" x1="0" y1="0" x2="0" y2="1">
      <stop offset="0" stop-color="#9fb3c7"/>
      <stop offset="1" stop-color="#4c5a68"/>
    </linearGradient>
    <linearGradient id="title-fill" x1="0" y1="0" x2="1" y2="1">
      <stop offset="0" stop-color="#ffffff"/>
      <stop offset="0.55" stop-color="#ffffff"/>
      <stop offset="1" stop-color="#bfe4ff"/>
    </linearGradient>
    <clipPath id="frame"><rect width="1200" height="1205"/></clipPath>
  </defs>

  <g clip-path="url(#frame)">
    <!-- marina backdrop -->
    <rect class="backdrop" width="1200" height="1205" fill="url(#ocean)" role="img" aria-label="Sportfishing boat docked at a marina at dusk, tinted blue"/>

    <!-- brand badge -->
    <circle cx="148" cy="155" r="268" fill="var(--accent)" opacity="0.55"/>
    <circle cx="148" cy="155" r="226" fill="var(--accent-light)"/>
    <circle cx="148" cy="155" r="214" fill="var(--white)"/>
    <text class="brand-name" x="160" y="250" text-anchor="middle">Tidewake</text>
    <text class="brand-name" x="160" y="288" text-anchor="middle">Charter Angling</text>

    <text class="site-url" x="1118" y="100" text-anchor="end">www.tidewakecharterangling,com</text>

    <!-- headline -->
    <text class="headline" x="598" y="515" text-anchor="middle" fill="url(#title-fill)">Canyon Fishing</text>
    <text class="headline" x="598" y="636" text-anchor="middle" fill="url(#title-fill)">&amp; Tuna Fishing</text>

    <!-- gallery frame -->
    <path d="M112 990 V760 Q112 700 172 700 H1025 Q1085 700 1085 760 V990" fill="none" stroke="var(--line)" stroke-width="2"/>
    <rect x="376" y="674" width="444" height="48" rx="24" fill="var(--accent)"/>
    <g class="camera-icon" fill="var(--white)">
      <rect x="398" y="684" width="34" height="26" rx="4"/>
      <rect x="407" y="680" width="14" height="6" rx="2"/>
      <circle cx="415" cy="697" r="8" fill="var(--accent)"/>
      <circle cx="415" cy="697" r="4.5"/>
    </g>
    <text class="tagline" x="440" y="708">with Memorable Capture</text>

    <!-- catch gallery -->
    <g class="catch-gallery">
      <path d="M145 865 A113 113 0 0 1 371 865 Z" fill="var(--accent)"/>
      <path d="M373 865 A113 113 0 0 0 599 865 Z" fill="var(--accent)"/>
      <path d="M596 865 A113 113 0 0 1 822 865 Z" fill="var(--accent)"/>
      <path d="M827 865 A113 113 0 0 0 1053 865 Z" fill="var(--accent)"/>

      <circle cx="272" cy="870" r="90" fill="none" stroke="var(--accent)" stroke-width="3"/>
      <circle cx="272" cy="870" r="82" fill="url(#catch)" stroke="var(--white)" stroke-width="4" role="img" aria-label="Angler on deck holding a bluefin tuna"/>

      <circle cx="500" cy="870" r="90" fill="none" stroke="var(--white)" stroke-width="3"/>
      <circle cx="500" cy="870" r="82" fill="url(#catch)" stroke="var(--accent)" stroke-width="4" role="img" aria-label="Two anglers at sea with a large tuna"/>

      <circle cx="697" cy="870" r="90" fill="none" stroke="var(--accent)" stroke-width="3"/>
      <circle cx="697" cy="870" r="82" fill="url(#catch)" stroke="var(--white)" stroke-width="4" role="img" aria-label="Angler in the cockpit holding up a tuna"/>

      <circle cx="922" cy="870" r="90" fill="none" stroke="var(--white)" stroke-width="3"/>
      <circle cx="922" cy="870" r="82" fill="url(#catch)" stroke="var(--accent)" stroke-width="4" role="img" aria-label="Angler on the dock with a landed tuna"/>
    </g>
  </g>
</svg>
</body>
</html>
```